Business Card Design

Bookkeeping-data entry, bank reconciliation and review. Business Associate, Tally Trim Partners
Payroll-PAYG, Superannuation, QUIVA and other Accounting softwares
BAS-NRB & PLCU registered BAS Agent
Training & Support-QUIVA Certified Advisor
Management reports-Regular detailed and described
Tax - Network of registered Tax Agents
Company and Trust Set up - Network of legal practitioners and corporate advisory group

Target Market(s)

Small to medium business and (individuals for income tax)

Industry/Entity Type

Legal

Contact Information for Business Card

Ledger Lark ABN 83 914 605 271, Darvin Kolestra BEc Grad Dip Acct FTMA Tel 03 9000 7281 M 04000 82 316 darvin@ledgerlark.example.au
12 Juniper Close Fernvale Vic 3999 ( in small font in right corner the following) :
Consultant: Harriet Dunmore FCA FCPA
Chartered Accountant
Registered Company Auditor
Registered Tax Agent

Font styles to use
Sans Serif

Colors
1f68af
ffc214
f37023
85cae6

Requirements
Nice to have
• Consultant: Harriet Dunmore FCA FCPA
Chartered Accountant
Registered Tax Agent
( only if possible at smaller font in the front of card)

```html
<!DOCTYPE html>
<html lang="en">
<head>
<meta charset="utf-8">
<title>Ledger Lark — Business Card</title>
<link rel="stylesheet" href="https://fonts.googleapis.com/css2?family=Nunito+Sans:wght@400;600;700&display=swap">
<style>
  :root {
    --brand-blue: #1f68af;
    --brand-blue-deep: #1a4f99;
    --brand-sky: #85cae6;
    --brand-gold: #ffc214;
    --brand-orange: #f37023;
    --ink: #2b3a55;
    --ink-soft: #5d6b80;
    --assoc-purple: #6a5a9c;
    --badge-teal: #1d4f5e;
    --stage: #f1f2f4;
  }
  * { box-sizing: border-box; margin: 0; padding: 0; }
  html, body { width: 1200px; height: 900px; overflow: hidden; }
  body {
    background: var(--stage);
    font-family: "Nunito Sans", Arial, sans-serif;
    color: var(--ink);
    position: relative;
  }
  .card {
    position: absolute;
    top: 288px;
    width: 540px;
    height: 324px;
    background: linear-gradient(180deg, #ffffff 0%, #f6f7f9 100%);
    border-radius: 26px;
    box-shadow: 0 10px 30px rgba(0,0,0,0.12);
    overflow: hidden;
  }
  .card--front { left: 40px; }
  .card--back { left: 620px; }

  /* Front */
  .brand { position: absolute; left: 28px; top: 30px; display: flex; align-items: center; gap: 18px; }
  .brand__dot {
    width: 82px; height: 82px; border-radius: 50%;
    background: radial-gradient(circle at 40% 35%, var(--brand-gold), var(--brand-orange));
  }
  .brand__name { font-size: 36px; font-weight: 600; color: var(--brand-blue); letter-spacing: 0.5px; }

  .holder { position: absolute; left: 28px; top: 138px; }
  .holder__name { font-size: 15px; font-weight: 600; color: var(--brand-blue); }
  .holder__creds { font-size: 10px; color: var(--ink-soft); margin-top: 1px; }

  .contact { position: absolute; left: 28px; top: 184px; list-style: none; }
  .contact li { display: flex; align-items: center; gap: 5px; font-size: 12px; line-height: 17px; color: var(--ink); white-space: nowrap; }
  .contact svg { width: 11px; height: 11px; fill: var(--brand-blue-deep); flex: none; }
  .contact .contact__abn { padding-left: 16px; font-size: 11px; }

  .consultant { position: absolute; right: 30px; top: 238px; text-align: right; }
  .consultant__name { font-size: 13px; font-weight: 600; color: var(--brand-blue); }
  .consultant__role { font-size: 9.5px; color: var(--ink-soft); line-height: 12px; }

  .swoosh { position: absolute; left: 0; bottom: 0; width: 540px; height: 70px; }

  /* Back */
  .emblem { position: absolute; left: 0; right: 0; top: 92px; display: flex; justify-content: center; align-items: center; gap: 20px; }
  .emblem__dot {
    width: 110px; height: 110px; border-radius: 50%;
    background: radial-gradient(circle at 40% 35%, var(--brand-gold), var(--brand-orange));
  }
  .emblem__name { font-size: 34px; font-weight: 600; color: var(--brand-blue); }

  .assoc { position: absolute; left: 28px; bottom: 40px; display: flex; align-items: center; gap: 10px; }
  .assoc__badge { width: 26px; height: 30px; background: var(--assoc-purple); border-radius: 3px 3px 12px 12px; }
  .assoc__name { font-size: 10px; line-height: 12px; color: var(--assoc-purple); }
  .assoc__tag { font-size: 6px; color: var(--ink-soft); margin-top: 2px; }

  .partner { position: absolute; right: 24px; bottom: 64px; display: flex; align-items: center; gap: 8px; }
  .partner__dot { width: 30px; height: 30px; border-radius: 50%; background: var(--brand-sky); }
  .partner__name { font-size: 12px; font-weight: 600; color: var(--brand-sky); }
  .partner__badge { width: 30px; height: 30px; border-radius: 50%; background: var(--badge-teal); }
</style>
</head>
<body>

<section class="card card--front" aria-label="Business card front">
  <div class="brand">
    <span class="brand__dot"></span>
    <span class="brand__name">Ledger Lark</span>
  </div>

  <div class="holder">
    <p class="holder__name">Darvin Kolestra</p>
    <p class="holder__creds">BEc Grad Dip Acct FTMA</p>
  </div>

  <ul class="contact">
    <li><svg viewBox="0 0 24 24"><path d="M6.6 10.8a15 15 0 0 0 6.6 6.6l2.2-2.2c.3-.3.7-.4 1-.2 1.1.4 2.3.6 3.6.6.6 0 1 .4 1 1V20c0 .6-.4 1-1 1A17 17 0 0 1 3 4c0-.6.4-1 1-1h3.5c.6 0 1 .4 1 1 0 1.3.2 2.5.6 3.6.1.3 0 .7-.2 1z"/></svg>03 9000 7281</li>
    <li><svg viewBox="0 0 24 24"><path d="M7 1h10a2 2 0 0 1 2 2v18a2 2 0 0 1-2 2H7a2 2 0 0 1-2-2V3a2 2 0 0 1 2-2zm0 3v14h10V4z"/></svg>04000 82 316</li>
    <li><svg viewBox="0 0 24 24"><path d="M2 5h20v14H2zm2 2v.5l8 5 8-5V7z"/></svg>darvin@ledgerlark.example.au</li>
    <li><svg viewBox="0 0 24 24"><path d="M12 3 1 12h3v9h6v-6h4v6h6v-9h3z"/></svg>12 Juniper Close Fernvale Vic 3999</li>
    <li class="contact__abn">ABN 83 914 605 271</li>
  </ul>

  <div class="consultant">
    <p class="consultant__name">Consultant: Harriet Dunmore</p>
    <p class="consultant__role">FCA FCPA Chartered Accountant</p>
    <p class="consultant__role">Registered Company Auditor Registered Tax Agent</p>
  </div>

  <svg class="swoosh" viewBox="0 0 540 70" preserveAspectRatio="none" aria-hidden="true">
    <defs>
      <linearGradient id="bandBlue" x1="0" x2="1" y1="0" y2="0">
        <stop offset="0" stop-color="#1a4f99"/>
        <stop offset="0.45" stop-color="#4f8fd0"/>
        <stop offset="1" stop-color="#1f68af"/>
      </linearGradient>
      <linearGradient id="bandGold" x1="0" x2="1" y1="0" y2="0">
        <stop offset="0" stop-color="#ffc214"/>
        <stop offset="1" stop-color="#f37023"/>
      </linearGradient>
    </defs>
    <path d="M0 18 C 180 24, 360 38, 540 44 L540 48 C 360 42, 180 28, 0 22 Z" fill="url(#bandGold)"/>
    <path d="M0 24 C 180 30, 360 44, 540 50 L540 70 L0 70 Z" fill="url(#bandBlue)"/>
  </svg>
</section>

<section class="card card--back" aria-label="Business card back">
  <div class="emblem">
    <span class="emblem__dot"></span>
    <span class="emblem__name">Ledger Lark</span>
  </div>

  <div class="assoc">
    <span class="assoc__badge"></span>
    <div>
      <p class="assoc__name">Professional Ledger &amp;<br>Compliance Union</p>
      <p class="assoc__tag">Trusted Small Business Support</p>
    </div>
  </div>

  <div class="partner">
    <span class="partner__dot"></span>
    <span class="partner__name">QUIVA</span>
    <span class="partner__badge"></span>
  </div>
</section>

</body>
</html>
```